high end contractor

high end contracting company we do all phases of construction kitchen,bathrooms,etc... please look at my website before you design www.harborkeybuild.com

would love some sort of lines or logo or both

Industry/Entity Type

Construction

Contact Information for Business Card

company name: oak & meridian contracting address: 318 fenwick st mount Vernon ny 10552 email: harborkeybuild@mailbrook.com website: www.harborkeybuild.com office#: 914-208-3916 fax#: 914-208-5523 dominic valtersen mobile# 917-526-0389

```html
<!DOCTYPE html>
<html lang="en">
<head>
<meta charset="utf-8">
<title>Oak &amp; Meridian Renovations — Business Cards</title>
<link rel="stylesheet" href="https://fonts.googleapis.com/css2?family=Cabin:wght@400;600&family=Arimo:ital@1&display=swap">
<style>
  :root {
    --page: #ffffff;
    --card: #1c1c1c;
    --teal: #4cc3bf;
    --white: #f4f4f4;
    --icon: #e8e8e8;
    --photo-dark-a: #2a2a2a;
    --photo-dark-b: #5a5a58;
    --photo-warm-a: #6b4a33;
    --photo-warm-b: #c9c2b4;
    --photo-warm-c: #a8b04a;
  }
  * { box-sizing: border-box; margin: 0; padding: 0; }
  html, body { width: 1200px; height: 1000px; overflow: hidden; background: var(--page); }
  .canvas { position: relative; width: 1200px; height: 1000px; }

  .card {
    position: absolute;
    width: 640px;
    height: 336px;
    background: var(--card);
    border-radius: 22px;
    overflow: hidden;
  }
  .card--contact { left: 100px; top: 126px; }
  .card--brand { left: 472px; top: 416px; height: 352px; }

  .brand-name {
    font-family: "Cabin", sans-serif;
    font-size: 20px;
    letter-spacing: 0.6px;
    color: var(--white);
    font-weight: 400;
  }
  .brand-name__lead { color: var(--teal); font-weight: 600; }

  /* contact side */
  .interior-photo--contact {
    position: absolute; inset: 0;
    background:
      radial-gradient(ellipse at 70% 65%, rgba(150,150,148,0.55), transparent 55%),
      linear-gradient(160deg, var(--photo-dark-a) 0%, #202020 40%, var(--photo-dark-b) 100%);
  }
  .card--contact .brand-name {
    position: absolute; left: 110px; top: 36px;
  }
  .contact-line {
    position: absolute;
    font-family: "Arimo", sans-serif;
    font-style: italic;
    font-size: 16px;
    color: var(--teal);
    white-space: nowrap;
    line-height: 1;
  }
  .contact-icon { position: absolute; width: 15px; height: 15px; }
  .contact-icon path, .contact-icon rect { fill: none; stroke: var(--icon); stroke-width: 1.4; }
  .contact-icon .solid { fill: var(--icon); stroke: none; }

  /* brand side */
  .interior-photo--brand {
    position: absolute; left: 0; top: 0; width: 345px; height: 100%;
    background:
      radial-gradient(ellipse at 45% 82%, var(--photo-warm-c), transparent 32%),
      linear-gradient(180deg, #8b8278 0%, var(--photo-warm-b) 38%, #7a5a40 70%, var(--photo-warm-a) 100%);
  }
  .slat-edge { position: absolute; left: 0; top: 0; width: 345px; height: 100%; }
  .slat-edge rect { fill: var(--card); }
  .card--brand .brand-name {
    position: absolute; right: 24px; top: 116px;
    text-align: right; font-size: 22px; line-height: 33px;
  }
</style>
</head>
<body>
<div class="canvas">

  <section class="card card--contact">
    <div class="interior-photo--contact" role="img" aria-label="Dark photograph of a modern living room with white lounge chairs and a fireplace"></div>
    <h1 class="brand-name"><span class="brand-name__lead">OAK &amp; MERIDIAN</span> RENOVATIONS</h1>

    <svg class="contact-icon" style="left:62px;top:191px" viewBox="0 0 16 16" aria-hidden="true">
      <path d="M2 8 L8 2.5 L14 8 M4 7 V14 H12 V7 M7 14 V10 H9 V14"/>
    </svg>
    <p class="contact-line" style="left:87px;top:191px">318 Fenwick Street</p>
    <p class="contact-line" style="left:81px;top:213px">Elmwood Ridge, NY 10874</p>

    <svg class="contact-icon" style="left:45px;top:241px" viewBox="0 0 16 16" aria-hidden="true">
      <path d="M2 6 L8 2 L14 6 V13 H2 Z M2 6 L8 10 L14 6"/>
    </svg>
    <p class="contact-line" style="left:69px;top:241px">email: harborkeybuild@mailbrook.com</p>

    <svg class="contact-icon" style="left:38px;top:272px" viewBox="0 0 16 16" aria-hidden="true">
      <path class="solid" d="M4 1.5 C2.5 2.5 2 4 2.5 6.5 C3.5 10.5 6 13.5 9 14.5 C10.5 15 11.5 14.5 12 13.5 L10 10.5 L8.5 11.2 C7 10.3 5.8 8.5 5.5 6.8 L7 6 L6 2 Z"/>
    </svg>
    <p class="contact-line" style="left:60px;top:272px">914-208-3916</p>

    <svg class="contact-icon" style="left:194px;top:272px" viewBox="0 0 16 16" aria-hidden="true">
      <rect x="4" y="1.5" width="8" height="4"/>
      <rect x="1.5" y="5.5" width="13" height="6" class="solid"/>
      <rect x="4" y="10" width="8" height="4.5"/>
    </svg>
    <p class="contact-line" style="left:218px;top:272px">914-208-5523</p>

    <svg class="contact-icon" style="left:350px;top:270px" viewBox="0 0 16 18" aria-hidden="true">
      <rect x="4.5" y="3" width="7" height="13.5" rx="1"/>
      <rect x="6" y="5" width="4" height="4" class="solid"/>
      <path d="M10 3 V0.5"/>
    </svg>
    <p class="contact-line" style="left:370px;top:272px">917-526-0389</p>
  </section>

  <section class="card card--brand">
    <div class="interior-photo--brand" role="img" aria-label="Photograph of a bright modern interior with wood floors and green chairs, seen through horizontal slats"></div>
    <svg class="slat-edge" viewBox="0 0 345 352" preserveAspectRatio="none" aria-hidden="true">
      <rect x="300" y="0" width="45" height="14"/>
      <rect x="250" y="28" width="95" height="10"/>
      <rect x="320" y="50" width="25" height="12"/>
      <rect x="270" y="74" width="75" height="10"/>
      <rect x="310" y="98" width="35" height="12"/>
      <rect x="230" y="122" width="115" height="10"/>
      <rect x="325" y="146" width="20" height="12"/>
      <rect x="280" y="170" width="65" height="10"/>
      <rect x="305" y="194" width="40" height="12"/>
      <rect x="260" y="218" width="85" height="10"/>
      <rect x="318" y="242" width="27" height="12"/>
      <rect x="290" y="266" width="55" height="10"/>
      <rect x="312" y="290" width="33" height="12"/>
      <rect x="300" y="314" width="45" height="38"/>
      <rect x="0" y="10" width="60" height="10"/>
      <rect x="20" y="58" width="50" height="10"/>
      <rect x="0" y="106" width="30" height="10"/>
      <rect x="40" y="154" width="70" height="10"/>
      <rect x="10" y="202" width="40" height="10"/>
    </svg>
    <h2 class="brand-name"><span class="brand-name__lead">OAK &amp; MERIDIAN</span><br>RENOVATIONS</h2>
  </section>

</div>
</body>
</html>
```